Law Firm Needs a new Website Design

We need a new website design for our law firm located in Manhattan (Law Offices of Tobias R. Venkland, PLLC).
We have an existing logo that we will to continue using, which can be found in www.VenklandLaw.example.
The Prime Counsel, Top Advocates Logo should also be reflected near the bottom of the Home page.
The website will be 6 pages.

Deliverables:
I want a
1) home page,
2) About Us/Practice Areas page,
3) attorneys,
4) News and Articles page, and
5) Contact and Directions/Privacy Policy page.

The colors of my logo should be in the website.
I also like a touch of black and red.

The website should project "excellence."
We seek to provide the highest quality legal services.
We handle estate planning, wills, trusts, planning for people with disabilities, asset protection and preservation, Medicaid planning, hospital safe discharge, nursing home placement, powers of attorney, health care proxies, living wills, guardianships, probate, estate administration and related litigation.

I would like the colors of my Logo used (including shading where appropriate).
I also want some black on the borders and/or bottom and some red touches throughout the page.

My Logo should appear everywhere that "Law Offices Of Tobias R. Venkland, PLLC" appears.
I want the badges for Prime counsel, Top Advocates, Top Legal Practices, and ZELQ on the Home page.
I do not want too much text on the home page.

We would also like the website to have coding.
The final design should also communicate quality, expertise and stability.
Great start so far by the people who submitted designs.
Thank you.

Industry/Entity Type

Law Firm

Coding

Coded - Design and coding required

Number of Pages Required

5+ page

Colors
3276b5
ec1f27
474747

Requirements
Must have
• Please use my logo each time you mention Law Offices of Tobias R. Venkland, PLLC. Please include the Primecounsel, Top Advocates, Top Legal Practices and Zelq rating Badges on the web home page. I only wish to be contacted by phone. I am not including testimonials and am only using the New York City address.
Nice to have
• Prefer illustrations to photos regarding practice areas
Should not have
• Testimonials, contact me by email, free consultation.

```html
<!DOCTYPE html>
<html lang="en">
<head>
<meta charset="utf-8">
<title>Law Offices of Tobias R. Venkland, PLLC</title>
<link href="https://fonts.googleapis.com/css2?family=Noto+Serif:ital,wght@0,400;0,700;1,400&family=Open+Sans:wght@400;600;700&display=swap" rel="stylesheet">
<style>
:root{
  --blue:#3276b5;
  --red:#ec1f27;
  --dark:#474747;
  --ink:#2b2b2b;
  --nav:#333333;
  --footer:#3b3b3b;
  --grey-bg:#f2f2f2;
  --muted:#8a8a8a;
  --line:#dddddd;
  --white:#ffffff;
}
*{box-sizing:border-box;margin:0;padding:0}
html,body{width:1200px;height:4905px;overflow:hidden}
body{position:relative;background:var(--white);font-family:"Open Sans",Arial,sans-serif;color:var(--dark);font-size:13px}
.photo{position:absolute}

/* header */
.site-header{position:absolute;left:0;top:0;width:1200px;height:170px;background:var(--white)}
.brand-block{position:absolute;left:0;top:0;width:500px;height:170px;background:var(--red);clip-path:polygon(0 0,100% 0,88% 100%,0 100%)}
.brand{position:absolute;left:60px;top:48px;display:flex;align-items:center;gap:16px}
.brand-mark{width:54px;height:54px;border:2px solid var(--white)}
.brand-name{font-family:"Noto Serif",Georgia,serif;color:var(--white);font-size:21px;line-height:1.3;font-weight:400}
.top-links{position:absolute;left:545px;top:14px;display:flex;gap:60px;font-size:19px;color:var(--ink)}
.top-links span:first-child{border-bottom:2px solid var(--red)}
.top-rule{position:absolute;left:520px;top:58px;width:680px;height:1px;background:var(--line)}
.contact-item{position:absolute;top:80px;display:flex;gap:12px;align-items:center}
.contact-item .ic{width:34px;height:34px;border-radius:50%;background:var(--red)}
.contact-item b{display:block;font-size:11px;color:var(--ink)}
.contact-item small{font-size:11px;color:var(--red)}
.social-box{position:absolute;left:890px;top:80px;width:150px;height:34px;background:var(--red);display:flex;justify-content:center;align-items:center;gap:18px}
.social-box i{width:14px;height:14px;border-radius:50%;background:var(--white);display:block}

.main-nav{position:absolute;left:163px;top:170px;width:1037px;height:46px;background:var(--nav);display:flex;align-items:center;font-size:15px;font-weight:600;color:var(--white)}
.main-nav span{padding:0 28px;height:46px;line-height:46px;border-right:1px solid #4a4a4a}
.main-nav .active{background:var(--red)}

/* hero */
.hero{left:0;top:216px;width:1200px;height:487px;background:linear-gradient(90deg,#d9d4cc 0%,#e6e8e6 35%,#f4f4f2 60%,#ffffff 100%)}
.hero-figure{left:150px;top:216px;width:450px;height:487px;background:linear-gradient(180deg,#c9a98f 0%,#6b5b55 45%,#2a2a2e 100%);opacity:.55}
.hero-text{position:absolute;right:160px;top:352px;text-align:right}
.hero-text .kicker{font-family:"Noto Serif",Georgia,serif;color:var(--blue);font-size:28px;border-bottom:2px solid var(--blue);display:inline-block}
.hero-text h1{font-family:"Noto Serif",Georgia,serif;font-size:54px;line-height:1.1;color:var(--ink);font-weight:700}
.hero-text h1 .red{color:var(--red)}
.hero-btn{display:inline-block;margin-top:14px;background:var(--red);color:var(--white);font-size:11px;font-weight:700;padding:8px 24px}

.feature-bar{position:absolute;left:163px;top:664px;width:877px;height:131px;background:var(--blue);display:flex;align-items:center;padding:0 30px;gap:30px}
.feature{display:flex;gap:16px;align-items:flex-start;flex:1}
.feature .fi{width:58px;height:58px;background:var(--white);flex:none;display:flex;align-items:center;justify-content:center}
.feature h4{color:var(--white);font-size:15px;font-weight:600;margin-bottom:6px}
.feature p{color:#dce8f5;font-size:11px;line-height:1.4}

/* section heading */
.sec-head{position:absolute;left:0;width:1200px;text-align:center}
.sec-head .chev{display:block;margin:0 auto 4px}
.sec-head h2{font-family:"Noto Serif",Georgia,serif;font-size:24px;color:var(--ink);font-weight:700;letter-spacing:1px}
.sec-head .bar{width:44px;height:3px;background:var(--red);margin:10px auto 14px}
.sec-head p{font-size:11px;color:var(--muted);line-height:1.6}

/* about */
.tabs{position:absolute;left:163px;top:1045px;width:212px}
.tab{height:56px;border:1px solid var(--line);border-bottom:none;display:flex;align-items:center;gap:14px;padding-left:24px;font-family:"Noto Serif",Georgia,serif;font-size:15px;color:var(--ink)}
.tab:last-child{border-bottom:1px solid var(--line)}
.tab.active{color:var(--red);border-left:4px solid var(--red)}
.tab .ti{width:20px;height:20px;border:2px solid currentColor;border-radius:50%}
.about-copy{position:absolute;left:400px;top:1045px;width:335px;font-size:11px;line-height:1.65;color:var(--muted)}
.about-copy p{margin-bottom:12px}
.about-photo{left:748px;top:1045px;width:276px;height:205px;background:linear-gradient(160deg,#d8d3c9,#6b6157 60%,#2d2a28)}

/* practice */
.practice-bg{left:0;top:1325px;width:1200px;height:817px;background:var(--grey-bg)}
.card{position:absolute;width:272px}
.card .photo{left:0;top:0;width:272px;height:100%}
.card .panel{position:absolute;left:18px;top:22px;right:18px;bottom:22px;background:rgba(255,255,255,.94);text-align:center;padding:18px 8px}
.card .pi{width:30px;height:30px;margin:0 auto 8px}
.card h3{font-family:"Noto Serif",Georgia,serif;font-size:14px;color:var(--ink);line-height:1.45;margin-bottom:8px;white-space:nowrap}
.card p{font-size:10px;color:var(--muted);line-height:1.5}
.card .more{display:block;color:var(--red);font-size:10px;font-weight:700;margin-top:8px}
.btn-red{position:absolute;background:var(--red);color:var(--white);font-size:13px;font-weight:700;text-align:center}

/* banner */
.banner{left:0;top:2142px;width:1200px;height:376px;background:linear-gradient(90deg,#6e6a66 0%,#9a9590 40%,#b9b4ae 70%,#8a857f 100%)}
.banner-text{position:absolute;left:173px;top:2200px;color:var(--white)}
.banner-text h2{font-family:"Noto Serif",Georgia,serif;font-size:54px;line-height:1.15;font-weight:700}
.banner-text h3{font-family:"Noto Serif",Georgia,serif;font-size:22px;margin-top:10px}
.banner-phone{position:absolute;left:173px;top:2398px;width:332px;height:48px;background:var(--red);color:var(--white);font-size:22px;font-weight:700;display:flex;align-items:center;gap:24px;padding-left:26px;white-space:nowrap}

/* why */
.why{position:absolute;left:105px;top:2560px;width:470px}
.why h2{font-family:"Noto Serif",Georgia,serif;font-size:24px;color:var(--ink)}
.why .bar{width:44px;height:3px;background:var(--red);margin:10px 0 12px}
.why .lead{font-size:11px;color:var(--muted);line-height:1.6}
.why-grid{display:grid;grid-template-columns:1fr 1fr;gap:34px 40px;margin-top:28px}
.why-grid .wi{display:block;width:22px;height:22px;border:2px solid var(--blue);border-radius:50%;margin-bottom:10px}
.why-grid h4{font-size:16px;color:var(--ink);font-weight:600;margin-bottom:6px}
.why-grid p{font-size:10px;color:var(--muted);line-height:1.5}
.why-photo{left:598px;top:2518px;width:602px;height:452px;background:linear-gradient(135deg,#e9e9e9,#8c8c8c 50%,#3a3a3a)}

/* attorneys */
.attorney{position:absolute;top:3178px;width:180px;height:272px;background:#eeeeee}
.attorney .photo{left:0;top:0;width:180px;height:272px}
.attorney .tag{position:absolute;left:0;bottom:0;width:180px;height:66px;background:var(--red);clip-path:polygon(0 14px,100% 0,100% 100%,0 100%);color:var(--white);text-align:center;padding-top:22px}
.attorney .tag b{display:block;font-family:"Noto Serif",Georgia,serif;font-size:12px;letter-spacing:.5px}
.attorney .tag small{font-size:9px}

/* news */
.news-bg{left:0;top:3565px;width:1200px;height:621px;background:var(--grey-bg)}
.news{position:absolute;top:3767px;width:272px}
.news .photo{position:relative;width:272px;height:173px}
.news h3{font-family:"Noto Serif",Georgia,serif;font-size:14px;color:var(--ink);line-height:1.4;margin:18px 0 10px}
.news p{font-size:10px;color:var(--muted);line-height:1.5;height:60px}
.news .meta{display:flex;justify-content:space-between;border-top:1px solid var(--line);padding-top:10px;margin-top:20px;font-size:12px;color:var(--ink)}

/* trust */
.trust{position:absolute;left:173px;top:4245px;width:360px}
.trust h2{font-family:"Noto Serif",Georgia,serif;font-size:30px;color:var(--ink)}
.trust .bar{width:44px;height:3px;background:var(--red);margin:10px 0 12px}
.trust p{font-size:12px;color:var(--blue);line-height:1.5}
.badge{position:absolute}

/* footer */
.footer{left:0;top:4447px;width:1200px;height:458px;background:var(--footer)}
.footer-panel{left:834px;top:4447px;width:366px;height:458px;background:var(--blue);clip-path:polygon(18px 0,100% 0,100% 100%,0 100%)}
.f-col{position:absolute;top:4620px;color:#cfcfcf;font-size:10px;line-height:1.6}
.f-col h4{font-family:"Noto Serif",Georgia,serif;color:var(--white);font-size:20px;margin-bottom:4px}
.f-col .bar{width:34px;height:2px;background:var(--red);margin-bottom:10px}
.f-social{display:flex;gap:10px;margin-top:12px}
.f-social i{width:12px;height:12px;border-radius:50%;background:var(--red);display:block}
.f-news{position:absolute;left:870px;top:4500px;width:290px;color:var(--white)}
.f-phone{display:flex;align-items:center;gap:14px;font-size:17px;font-weight:600;margin-left:30px}
.f-phone i{width:28px;height:28px;border-radius:50%;background:var(--red);display:block}
.f-news h5{font-size:16px;font-weight:400;text-align:center;margin-top:26px}
.f-news h4{font-family:"Noto Serif",Georgia,serif;font-size:30px;text-align:center;letter-spacing:1px}
.f-news .bar{width:34px;height:2px;background:var(--red);margin:8px auto 22px}
.f-news label{font-size:11px;display:block;margin-bottom:6px}
.f-news .field{height:34px;background:var(--white)}
.f-news .sub{display:inline-block;margin-top:12px;background:var(--red);font-size:10px;font-weight:700;padding:8px 22px}
.f-bottom{position:absolute;left:0;top:4840px;width:1200px;height:65px;border-top:1px solid #555;font-size:11px;color:#bdbdbd}
.f-bottom .copy{position:absolute;left:173px;top:24px}
.f-bottom .links{position:absolute;left:895px;top:24px;display:flex;gap:14px;color:var(--white);font-weight:600}
</style>
</head>
<body>

<header class="site-header">
  <div class="brand-block">
    <div class="brand">
      <div class="brand-mark"></div>
      <div class="brand-name">Law Offices of<br>Tobias R. Venkland, PLLC</div>
    </div>
  </div>
  <nav class="top-links"><span>Home</span><span>Attorneys</span><span>Contact and Directions</span></nav>
  <div class="top-rule"></div>
  <div class="contact-item" style="left:545px"><span class="ic"></span><div><b>CALL US</b><small>(212) 555-0148</small></div></div>
  <div class="contact-item" style="left:720px"><span class="ic"></span><div><b>FAX US</b><small>(212) 555-0193</small></div></div>
  <div class="social-box"><i></i><i></i><i></i></div>
</header>

<nav class="main-nav">
  <span class="active">Home</span><span>Practice Areas</span><span>Privacy &amp; Policy</span><span>Contact and Directions</span><span>News</span>
  <span style="border:none">
    <svg width="16" height="16" viewBox="0 0 16 16"><circle cx="6.5" cy="6.5" r="5" fill="none" stroke="#fff" stroke-width="2"/><line x1="10.5" y1="10.5" x2="15" y2="15" stroke="#fff" stroke-width="2"/></svg>
  </span>
</nav>

<section>
  <div class="photo hero" role="img" aria-label="Bright office interior background"></div>
  <div class="photo hero-figure" role="img" aria-label="Smiling attorney in a dark business suit"></div>
  <div class="hero-text">
    <div class="kicker">Experience</div>
    <h1>You Can<br><span class="red">Depend</span> &amp; <span class="red">Trust</span></h1>
    <span class="hero-btn">REQUEST A CASE EVALUATION</span>
  </div>
  <div class="feature-bar">
    <div class="feature"><span class="fi"><svg width="26" height="26" viewBox="0 0 26 26"><path d="M3 9 13 3l10 6-10 6z M6 13v6l7 4 7-4v-6" fill="none" stroke="#3276b5" stroke-width="2"/></svg></span><div><h4>Get Legal Help</h4><p>Trusted advice for every family<br>matter, from start to finish.</p></div></div>
    <div class="feature"><span class="fi"><svg width="26" height="26" viewBox="0 0 26 26"><circle cx="11" cy="11" r="7" fill="none" stroke="#3276b5" stroke-width="2.5"/><line x1="16" y1="16" x2="23" y2="23" stroke="#3276b5" stroke-width="2.5"/></svg></span><div><h4>Case Investigation</h4><p>We review each detail of your<br>case with careful attention.</p></div></div>
    <div class="feature"><span class="fi"><svg width="26" height="26" viewBox="0 0 26 26"><circle cx="13" cy="8" r="5" fill="#3276b5"/><path d="M3 24c0-6 4-9 10-9s10 3 10 9z" fill="#3276b5"/></svg></span><div><h4>Request For An Attorney</h4><p>Speak with an experienced<br>attorney by phone today.</p></div></div>
  </div>
</section>

<section>
  <div class="sec-head" style="top:870px">
    <svg class="chev" width="22" height="10" viewBox="0 0 22 10"><path d="M1 9 11 1l10 8" fill="none" stroke="#3276b5" stroke-width="3"/></svg>
    <h2>ABOUT US</h2><div class="bar"></div>
    <p>Our firm provides careful, dedicated legal counsel to families across New York City<br>with estate planning, elder law and related litigation matters.</p>
  </div>
  <div class="tabs">
    <div class="tab active"><span class="ti"></span>OUR MISSION</div>
    <div class="tab"><span class="ti"></span>OUR VISION</div>
    <div class="tab"><span class="ti"></span>OUR HISTORY</div>
  </div>
  <div class="about-copy">
    <p>We are committed to protecting what matters most to our clients. Each plan is built around your family, your assets and your goals, with clear guidance at every step of the process.</p>
    <p>Our attorneys bring decades of focused experience in wills, trusts, guardianships and Medicaid planning, serving clients throughout Manhattan.</p>
    <p>We believe quality legal service means listening first, explaining plainly and standing with you for the long term.</p>
  </div>
  <div class="photo about-photo" role="img" aria-label="Attorneys meeting with a client at a desk"></div>
</section>

<section>
  <div class="photo practice-bg"></div>
  <div class="sec-head" style="top:1393px">
    <svg class="chev" width="22" height="10" viewBox="0 0 22 10"><path d="M1 9 11 1l10 8" fill="none" stroke="#3276b5" stroke-width="3"/></svg>
    <h2>PRACTICE AREA</h2><div class="bar"></div>
    <p>We handle a full range of estate and elder law matters for individuals<br>and families, with care, precision and respect.</p>
  </div>

  <div class="card" style="left:173px;top:1543px;height:223px"><div class="photo" role="img" aria-label="Illustration for probate and estate administration" style="background:linear-gradient(135deg,#7a5a3a,#c9a26b)"></div><div class="panel"><h3>Probate and Estate<br>Administration</h3><p>Guiding families through the probate<br>process with clarity and care.</p><span class="more">Read More</span></div></div>
  <div class="card" style="left:464px;top:1543px;height:223px"><div class="photo" role="img" aria-label="Illustration for supplemental needs trusts" style="background:linear-gradient(135deg,#b88a5a,#e8d2b0)"></div><div class="panel"><svg class="pi" viewBox="0 0 30 30"><path d="M3 14 15 4l12 10v13H3z" fill="none" stroke="#3276b5" stroke-width="2"/></svg><h3>Supplemental Needs Trusts</h3><p>Protecting benefits for loved ones<br>with disabilities.</p><span class="more">Read More</span></div></div>
  <div class="card" style="left:755px;top:1543px;height:223px"><div class="photo" role="img" aria-label="Illustration for Medicaid planning" style="background:linear-gradient(135deg,#5a2a2a,#a04040)"></div><div class="panel"><h3>Medicaid Planning and<br>Assistance with the<br>Application Process</h3><p>Preserving assets while securing care.</p><span class="more">Read More</span></div></div>
  <div class="card" style="left:173px;top:1792px;height:235px"><div class="photo" role="img" aria-label="Illustration for guardianships" style="background:linear-gradient(135deg,#8a7a6a,#d8cfc3)"></div><div class="panel"><svg class="pi" viewBox="0 0 30 30"><rect x="3" y="7" width="24" height="16" fill="none" stroke="#3276b5" stroke-width="2"/><circle cx="15" cy="15" r="4" fill="#3276b5"/></svg><h3>Guardianships</h3><p>Securing care and decision making<br>for those who need support.</p><span class="more">Read More</span></div></div>
  <div class="card" style="left:464px;top:1792px;height:235px"><div class="photo" role="img" aria-label="Illustration for estate planning" style="background:linear-gradient(135deg,#c43a1a,#f0a030)"></div><div class="panel"><svg class="pi" viewBox="0 0 30 30"><circle cx="15" cy="15" r="11" fill="none" stroke="#3276b5" stroke-width="2"/><path d="M10 15h10M15 10v10" stroke="#3276b5" stroke-width="2"/></svg><h3>Estate Planning</h3><p>Wills, trusts and plans that<br>protect your family's future.</p><span class="more">Read More</span></div></div>
  <div class="card" style="left:755px;top:1792px;height:235px"><div class="photo" role="img" aria-label="Illustration for powers of attorney and health care proxies" style="background:linear-gradient(135deg,#2f6fb0,#a8cbe8)"></div><div class="panel"><h3>Powers of Attorney, Health<br>care Proxies and Other<br>Advanced Directives</h3><p>Plans for every stage of life.</p><span class="more">Read More</span></div></div>
  <div class="btn-red" style="left:518px;top:2050px;width:164px;height:43px;line-height:43px">VIEW ALL</div>
</section>

<section>
  <div class="photo banner" role="img" aria-label="Distressed person sitting against a concrete wall"></div>
  <div class="banner-text"><h2>Bad Things<br>Happen</h2><h3>We Are Here To Help</h3></div>
  <div class="banner-phone"><svg width="20" height="20" viewBox="0 0 20 20"><path d="M4 1h4l2 5-3 2c1 2 3 4 5 5l2-3 5 2v4c0 1-1 2-2 2C9 18 2 11 2 3c0-1 1-2 2-2z" fill="#fff"/></svg>(212) - 555 - 0176</div>
</section>

<section>
  <div class="why">
    <h2>Why Venkland Law</h2><div class="bar"></div>
    <p class="lead">Clients choose us for focused experience, steady guidance and attorneys<br>who treat every family matter with the care it deserves.</p>
    <div class="why-grid">
      <div><span class="wi"></span><h4>Huge Experience</h4><p>Decades of practice in estate<br>and elder law matters.</p></div>
      <div><span class="wi"></span><h4>Skilled Attorneys</h4><p>A trusted team with deep<br>knowledge of New York law.</p></div>
      <div><span class="wi"></span><h4>Amazing Strategy</h4><p>Plans tailored to your family<br>and your long term goals.</p></div>
      <div><span class="wi"></span><h4>Low Cost</h4><p>Clear, fair fees with no<br>surprises along the way.</p></div>
    </div>
  </div>
  <div class="photo why-photo" role="img" aria-label="Group of attorneys in business suits"></div>
</section>

<section>
  <div class="sec-head" style="top:3034px">
    <svg class="chev" width="22" height="10" viewBox="0 0 22 10"><path d="M1 9 11 1l10 8" fill="none" stroke="#3276b5" stroke-width="3"/></svg>
    <h2>OUR ATTORNEYS</h2><div class="bar"></div>
    <p>Meet the attorneys who bring experience, care and dedication<br>to every client we represent.</p>
  </div>
  <div class="attorney" style="left:173px"><div class="photo" role="img" aria-label="Portrait of attorney Marcus Hale" style="background:linear-gradient(180deg,#e4e4e4,#9a9a9a)"></div><div class="tag"><b>MARCUS HALE</b><small>Founder &amp; CEO</small></div></div>
  <div class="attorney" style="left:392px"><div class="photo" role="img" aria-label="Portrait of attorney Dorian Pell" style="background:linear-gradient(180deg,#e4e4e4,#8e8e8e)"></div><div class="tag"><b>DORIAN PELL</b><small>Senior Partner</small></div></div>
  <div class="attorney" style="left:611px"><div class="photo" role="img" aria-label="Portrait of attorney Elise Marrow" style="background:linear-gradient(180deg,#e8e4e0,#9a918a)"></div><div class="tag"><b>ELISE MARROW</b><small>Family Law Attorney</small></div></div>
  <div class="attorney" style="left:830px"><div class="photo" role="img" aria-label="Portrait of attorney Nadia Corven" style="background:linear-gradient(180deg,#e8e4e0,#8a8078)"></div><div class="tag"><b>NADIA CORVEN</b><small>Associate Attorney</small></div></div>
  <div class="btn-red" style="left:530px;top:3466px;width:140px;height:43px;line-height:43px">VIEW ALL</div>
</section>

<section>
  <div class="photo news-bg"></div>
  <div class="sec-head" style="top:3616px">
    <svg class="chev" width="22" height="10" viewBox="0 0 22 10"><path d="M1 9 11 1l10 8" fill="none" stroke="#3276b5" stroke-width="3"/></svg>
    <h2>LEGAL NEWS</h2><div class="bar"></div>
    <p>Updates and articles on estate planning, elder law<br>and matters affecting New York families.</p>
  </div>
  <article class="news" style="left:173px"><div class="photo" role="img" aria-label="Group of officials at a press event" style="background:linear-gradient(135deg,#3a3a44,#8a8a90)"></div><h3>Court Gives Final Approval To<br>Students and Citizens</h3><p>A recent ruling clarifies how courts review<br>settlements that affect families and the<br>rights of individuals in New York.</p><div class="meta"><span>December 11, 2015</span><span>Continue &gt;</span></div></article>
  <article class="news" style="left:464px"><div class="photo" role="img" aria-label="Business people shaking hands" style="background:linear-gradient(135deg,#e8e8e8,#5a5a5a)"></div><h3>Harlow &amp; Finch opens Florida legal<br>support centre to its customer</h3><p>The firm expands its support services<br>with a new centre designed to serve<br>clients more quickly and efficiently.</p><div class="meta"><span>January 04, 2016</span><span>Continue &gt;</span></div></article>
  <article class="news" style="left:755px"><div class="photo" role="img" aria-label="Figures with red umbrellas under a blue sky" style="background:linear-gradient(180deg,#6f9ccc,#c9d9e6 60%,#5e6a3e)"></div><h3>Brightmoor to push flexi-lawyers<br>to international network</h3><p>Flexible legal staffing is growing as<br>firms look for new ways to meet client<br>demand across many markets.</p><div class="meta"><span>January 16, 2016</span><span>Continue &gt;</span></div></article>
</section>

<section>
  <div class="trust"><h2>A House of Trust</h2><div class="bar"></div><p>Families across Manhattan rely on our firm for<br>steady guidance, honest counsel and results<br>that protect what matters most to them.</p></div>
  <div class="badge" style="left:668px;top:4232px;width:96px;height:70px;background:#1f3f73;border:3px solid #c9c9c9"></div>
  <div class="badge" style="left:580px;top:4340px;width:146px;height:40px;background:#e6e6e6;border:2px solid #474747"></div>
  <div class="badge" style="left:880px;top:4340px;width:150px;height:44px;background:#eef3f9;border-left:6px solid #3276b5"></div>
</section>

<footer>
  <div class="photo footer"></div>
  <div class="photo footer-panel"></div>
  <div class="brand" style="left:173px;top:4485px"><div class="brand-mark"></div><div class="brand-name">Law Offices of<br>Tobias R. Venkland, PLLC</div></div>
  <div class="f-col" style="left:173px;width:260px"><h4>About Us</h4><div class="bar"></div>We provide dedicated estate planning and elder law<br>counsel to families across New York City.<div class="f-social"><i></i><i></i><i></i><i></i><i></i></div></div>
  <div class="f-col" style="left:470px;width:300px"><h4>Contact Us</h4><div class="bar"></div>250 West 40th Street, Suite 1200, New York,<br>NY 10018<br><br><span style="color:var(--red)">&#9679;</span> (212) 555-0148</div>
  <div class="f-news">
    <div class="f-phone"><i></i>(212) 555-0148</div>
    <h5>Subscribe to our</h5><h4>NEWSLETTER</h4><div class="bar"></div>
    <label>Your Email here</label><div class="field"></div>
    <span class="sub">SUBSCRIBE</span>
  </div>
  <div class="f-bottom"><span class="copy">Copyright © 2016 Law Offices of Tobias R. Venkland, PLLC.</span><span class="links"><span>Terms of Use</span><span>Privacy Policy</span><span>Advertise</span><span>Contact</span></span></div>
</footer>

</body>
</html>
```